Our company TrulaPay, an online processor of payments is seeking talented submissions for our website redesign. The winning design will be chopped up and converted into a WordPress theme to allow for easy content additions and updates.

We are looking for modern designs that rival current websites in our industry (plimo.example, zanquetto.example, holvix.example, brandle.example, quillmarkcharges.example, evensplitcharges.example, KoboRun.example).

Our company is seeking to expand our reach to software developers and engineers who are either integrating our payment platform into their offerings or are engineering a custom solution for the company they work for and are in need of a payment platform such as our own.

We currently work with hundreds of different business partners whom either resell our services or integrate our processing capabilities into their software (which they sell). We also must communicate effectively to end users, businesses, who seek us out directly for their payment processing needs.

We are open to different color schemes but would ultimately like them to be somewhat inline with our current logo (see attached). Our website needs to instill security and confidence to any current and/or potential user as we are trusted with private and sensitive information.

We are seeking submissions from qualified; individual freelancers, freelance teams, and agencies who can attack this project in its entirety. Since this project is a total redesign, we would like submissions that have the capability to design any custom graphics, icons, buttons, and illustrations in line with our industry, capabilities, offerings, and content. We are looking for someone to design our new website and would prefer a vendor who can also help us to design elements (graphics, illustrations, charts, workflows) within our website.

Designs will be converted into a wordpress theme and we would like to utilize widgets for as many areas as possible to make editing and updating easy.

We are seeking the creation of a few unique pages but many of the pages for the majority of our content will just be internal content pages which will be duplicated.

We will likely contract with the winning submission for future work.

Please see Design Reference Document for more information

Target Market(s)

Resellers
Merchant Service Providers
Software Developers
Independent Sales Organizations (ISOs)
App Builders
Mobile App Builders
Independent Software Developers
Organizational Software Developers
Businesses who need to accept payments
Governments
Municipalities
Schools
DMVs
Courts
Retailers
Medical Offices
Hosipitals
Clinics
Dr. Offices
Gyms
Churches
Non-Profits
Software Companies
Technology Companies
Startups

• Logo cannot change drastically.

```html
<!DOCTYPE html>
<html lang="en">
<head>
<meta charset="utf-8">
<title>TrulaPay — Payment Processing</title>
<link rel="stylesheet" href="https://fonts.googleapis.com/css2?family=Open+Sans:wght@400;600;700&family=Nunito+Sans:wght@400;700;800&display=swap">
<style>
:root{
  --topbar:#e9e9e9;
  --band:#33729f;
  --ink:#1d1d1d;
  --nav:#9a9a9a;
  --brand-blue:#1b2f8f;
  --brand-red:#d3202a;
  --login:#4a8fbd;
  --headline:#2f4a5c;
  --sub:#7d8790;
  --body:#6f6f6f;
  --rule:#dcdcdc;
  --footer:#e8e8e8;
  --footer-panel:#dedede;
  --btn-top:#55a7de;
  --btn-bot:#2f7fc0;
  --card-top:#e4f0f9;
}
*{box-sizing:border-box;margin:0;padding:0}
html,body{width:1191px;height:1200px;overflow:hidden;background:#fff}
body{font-family:"Open Sans",Arial,sans-serif;color:var(--ink);position:relative}
.container{position:absolute;left:140px;width:911px}

.topbar{position:absolute;top:0;left:0;width:1191px;height:29px;background:var(--topbar)}
.search{position:absolute;left:633px;top:4px;width:178px;height:21px;background:#fff;border:1px solid #bbb;border-radius:3px;font-size:12px;color:#444;padding:2px 6px}
.search svg{position:absolute;right:6px;top:4px}
.callus{position:absolute;left:830px;top:7px;font-size:11px;color:#666;letter-spacing:.2px}
.callus b{color:#222}
.topbar .contact{position:absolute;left:984px;top:7px;font-size:11.5px;font-weight:700;color:#222}

.header{position:absolute;top:29px;left:0;width:1191px;height:69px;background:#fff}
.logo{position:absolute;left:140px;top:20px;display:flex;align-items:center;gap:6px;font-size:25px;font-weight:600;color:var(--brand-blue)}
.logo .mark{width:10px;height:10px;background:var(--brand-red);border-radius:50%}
.nav{position:absolute;top:0;left:0;width:1191px;height:69px;font-size:12px;font-weight:700;color:var(--nav)}
.nav span{position:absolute;top:27px;white-space:nowrap}
.nav .active{color:var(--ink)}
.login{position:absolute;left:976px;top:21px;width:75px;height:28px;border-radius:4px;background:var(--login);color:#fff;font-size:13.5px;font-weight:700;text-align:center;line-height:28px;letter-spacing:.3px}

.band{position:absolute;top:98px;left:0;width:1191px;height:590px;background:var(--band)}
.card{position:absolute;top:48px;width:437px;height:498px;border-radius:4px;overflow:hidden;background:linear-gradient(#fff 0%,var(--card-top) 35%,#d7e8f5 100%);box-shadow:0 2px 6px rgba(0,0,0,.3)}
.card.merchants{left:140px}
.card.developers{left:614px}
.card h2{position:relative;z-index:1;margin-top:18px;text-align:center;font-size:15.5px;font-weight:600;line-height:21px;color:#111;padding:0 10px}
.card p{position:relative;z-index:1;text-align:center;font-size:13px;line-height:21.5px;color:#222;padding:0 28px;margin-top:18px}
.card p + p{margin-top:21px}
.photo{position:absolute;left:0;bottom:0;width:100%;height:240px}
.merchants .photo{background:linear-gradient(180deg,rgba(225,235,242,0) 0%,#cfd9e0 30%,#b7bfc5 60%,#9aa3a9 100%)}
.developers .photo{background:linear-gradient(180deg,rgba(225,235,242,0) 0%,#cdd4d8 30%,#b8b3ad 60%,#a7a39d 100%)}
.cta{position:absolute;top:420px;left:28px;width:257px;height:52px;border-radius:4px;background:linear-gradient(var(--btn-top),var(--btn-bot));color:#fff;font-size:17.5px;font-weight:700;box-shadow:0 2px 3px rgba(0,0,0,.3);display:flex}
.cta .label{flex:1;display:flex;align-items:center;justify-content:center;border-right:1px solid rgba(0,0,0,.2)}
.cta .chev{width:50px;display:flex;align-items:center;justify-content:center;border-left:1px solid rgba(255,255,255,.3)}

.intro{top:754px;text-align:center}
.intro h1{font-family:"Nunito Sans",Arial,sans-serif;font-size:35px;font-weight:700;color:var(--headline);letter-spacing:-.2px}
.intro .lead{font-family:"Nunito Sans",Arial,sans-serif;font-size:18px;color:var(--sub);margin-top:2px}
.intro hr{border:0;border-top:1px solid var(--rule);margin:18px 0 20px}
.intro .copy{font-family:"Nunito Sans",Arial,sans-serif;font-size:13.5px;line-height:23px;color:var(--body);margin-bottom:10px}

.footer{position:absolute;top:1021px;left:0;width:1191px;height:128px;background:var(--footer)}
.contact-panel{position:absolute;left:140px;top:0;width:215px;height:128px;background:var(--footer-panel);padding:20px 8px 20px 18px;font-size:12.5px;color:#444;line-height:17px;white-space:nowrap}
.contact-panel h3{font-size:13.5px;font-weight:700;color:#222;margin-bottom:6px}
.contact-panel .row span{display:inline-block;width:46px}
.links{position:absolute;top:27px;list-style:none;font-family:"Nunito Sans",Arial,sans-serif;font-size:13.5px;color:#555;line-height:26px}
.links.one{left:407px}.links.two{left:620px}
.share{position:absolute;left:936px;top:22px}
.share h3{font-size:13px;font-weight:700;color:#222;margin-bottom:6px}
.share .icons{display:flex;gap:5px}
.share .icons span{width:35px;height:34px;display:block}

.copyright{position:absolute;top:1166px;left:0;width:1191px;text-align:center;font-family:"Nunito Sans",Arial,sans-serif;font-size:12px;color:#444}
.copyright i{font-style:normal;margin:0 6px}
</style>
</head>
<body>
<div class="topbar">
  <div class="search">Search
    <svg width="12" height="12" viewBox="0 0 12 12"><circle cx="5" cy="5" r="3.8" fill="none" stroke="#111" stroke-width="1.8"/><line x1="7.8" y1="7.8" x2="11" y2="11" stroke="#111" stroke-width="2"/></svg>
  </div>
  <div class="callus">CALL US ON: <b>555 013 2046</b></div>
  <div class="contact">CONTACT</div>
</div>

<header class="header">
  <div class="logo">TrulaPay<span class="mark"></span></div>
  <nav class="nav">
    <span class="active" style="left:417px">HOME</span>
    <span style="left:475px">SOLUTIONS</span>
    <span style="left:567px">PARTNERS</span>
    <span style="left:651px">RESOURCES</span>
    <span style="left:742px">DEVELOPERS</span>
    <span style="left:840px">COMPANY</span>
    <span style="left:923px">BLOG</span>
  </nav>
  <div class="login">LOGIN</div>
</header>

<section class="band">
  <article class="card merchants">
    <h2>Merchants, Businesses,<br>I have a business, Online Payment Processing, SaaS</h2>
    <p>This interactive graphic box will convey to the website visitor that this is where you click if you are a business and need to get setup to accept payments for your business with us.</p>
    <p>Something along the lines of maybe some skyscrapers, maybe a business disctrict</p>
    <div class="photo" role="img" aria-label="Photo of business people in suits seated in a bright meeting room"></div>
    <div class="cta"><span class="label">Businesses Click Here</span><span class="chev"><svg width="14" height="22" viewBox="0 0 14 22"><polyline points="2,2 12,11 2,20" fill="none" stroke="#fff" stroke-width="3"/></svg></span></div>
  </article>
  <article class="card developers">
    <h2>Developers, I Develop Software, Software Application Developers, Payment Processing API</h2>
    <p>Software Developers, Start-ups. Users who are looking to integrate a payment platform into their; website, ERP, CMS, mobile solution, software offering, some type of advanced integration requiring a custom integration with a payment processing platform, PaaS.</p>
    <p>Something graphically that speaks to software engineers and developers. Initial thoughts were maybe some gears moving with source code or programming languages incorporated.</p>
    <div class="photo" role="img" aria-label="Photo of a smiling developer working at a laptop in an office"></div>
    <div class="cta"><span class="label">Davs Click Here</span><span class="chev"><svg width="14" height="22" viewBox="0 0 14 22"><polyline points="2,2 12,11 2,20" fill="none" stroke="#fff" stroke-width="3"/></svg></span></div>
  </article>
</section>

<section class="container intro">
  <h1>Payment Processing for the 21st Century.</h1>
  <p class="lead">TrulaPay provides the software, technology, and platform for multi-channel payment acceptance.</p>
  <hr>
  <p class="copy">Since 1992 we have been helping merchants streamline their payment acceptance. Whether your acceptance needs are online, at the poin-of-sale, or mobile; TrulaPay can help.</p>
  <p class="copy">We provide both “out-of -the-box ” and custom solutions for your company or organization to begin taking paymentsin line with your needs and desires.</p>
</section>

<footer class="footer">
  <div class="contact-panel">
    <h3>CONTACT INFORMATION</h3>
    <div>Lorem Ipsum. Proin gravida</div>
    <div class="row"><span>Phone:</span>555 013 2046</div>
    <div class="row"><span>Email:</span>info@trulapay.example</div>
  </div>
  <ul class="links one"><li>ACH Processing</li><li>eCheck Processing</li><li>Paper Check Processing</li></ul>
  <ul class="links two"><li>ACH Processing</li><li>eCheck Processing</li><li>Paper Check Processing</li></ul>
  <div class="share">
    <h3>SHARE</h3>
    <div class="icons">
      <span style="background:#3b5a9a" role="img" aria-label="Share button"></span>
      <span style="background:#2aa3e0" role="img" aria-label="Share button"></span>
      <span style="background:#1f73b0" role="img" aria-label="Share button"></span>
    </div>
  </div>
</footer>

<div class="copyright">Copyright © 2014 TrulaPay. All Rights Reserved<i>|</i>Privacy Policy<i>|</i>Terms of Use</div>
</body>
</html>
```